Biz Cards for Lumivale Associates

Lumivale Associates is seeking a single-sided business card that is more visually-appealing than our current design (see attached).

Notes:
- Our colors are blue & teal.
- Our tag line must be large enough to be easily read
- We don't necessarily need our address included (that's just the biz office)
- We'd like to add our email address: Lumivale512@brindlemail.net

Thanks!

Industry/Entity Type

Business

Contact Information for Business Card

Standard size
PSD file required w/ text on its own layer

Colors
86cfc6
3277b5

```html
<!DOCTYPE html>
<html lang="en">
<head>
<meta charset="utf-8">
<title>Lumivale Associates – Business Card</title>
<link href="https://fonts.googleapis.com/css2?family=Roboto:wght@400;500&family=Roboto+Condensed:wght@500&display=swap" rel="stylesheet">
<style>
  :root {
    --backdrop: #3b3b3d;
    --card: #1d1d1f;
    --card-edge: #2a2a2c;
    --gloss-light: #9a9a9c;
    --gloss-dark: #2c2c2e;
    --ink: #e6e6e6;
    --ink-soft: #c9c9c9;
    --teal: #1faa9d;
  }
  * { box-sizing: border-box; margin: 0; padding: 0; }
  html, body {
    width: 799px; height: 1200px; overflow: hidden;
    background: var(--backdrop);
  }
  .canvas {
    position: relative; width: 799px; height: 1200px;
    font-family: "Roboto", Arial, sans-serif;
  }
  .card {
    position: absolute; left: 80px; width: 640px; height: 366px;
    background: var(--card);
    border: 1px solid var(--card-edge);
    border-radius: 4px;
    overflow: hidden;
  }
  .card--front { top: 180px; }
  .card--back { top: 660px; }

  /* Front */
  .front-mark {
    position: absolute; inset: 0;
    display: flex; align-items: center; justify-content: center; gap: 18px;
  }
  .front-mark__dot {
    width: 22px; height: 22px; border-radius: 50%;
    background: var(--gloss-light);
  }
  .front-mark__name {
    font-family: "Roboto", Arial, sans-serif;
    font-weight: 500; font-size: 46px; letter-spacing: 2px;
    color: var(--gloss-light);
  }

  /* Back */
  .back-decor {
    position: absolute; left: 300px; top: 150px;
    width: 520px; height: 520px; border-radius: 50%;
    background: radial-gradient(circle at 45% 35%, #3a3a3c 0%, var(--gloss-dark) 55%, #202022 100%);
  }
  .wordmark {
    position: absolute; left: 36px; top: 34px;
    font-family: "Roboto", Arial, sans-serif;
    font-weight: 500; font-size: 30px; letter-spacing: 3px;
    color: var(--ink);
    text-transform: uppercase;
  }
  .person { position: absolute; left: 36px; top: 130px; }
  .person__name {
    font-family: "Roboto Condensed", "Arial Narrow", sans-serif;
    font-weight: 500; font-size: 25px; color: var(--teal);
  }
  .person__role { font-size: 13px; color: var(--ink-soft); margin-top: 2px; }
  .contacts {
    position: absolute; left: 36px; top: 200px;
    list-style: none; font-size: 15px; color: var(--ink-soft);
  }
  .contacts li { display: flex; align-items: center; gap: 10px; height: 25px; }
  .contacts svg { width: 14px; height: 14px; flex: none; }
  .contacts .accent { color: var(--teal); }
</style>
</head>
<body>
<main class="canvas">

  <section class="card card--front" aria-label="Card front">
    <div class="front-mark">
      <span class="front-mark__dot"></span>
      <span class="front-mark__name">Lumivale</span>
    </div>
  </section>

  <section class="card card--back" aria-label="Card back">
    <div class="back-decor" aria-hidden="true"></div>
    <div class="wordmark">Lumivale Associates Ltd</div>
    <div class="person">
      <div class="person__name">Marissa Okafor, RN</div>
      <div class="person__role">Mental Health Therapist</div>
    </div>
    <ul class="contacts">
      <li>
        <svg viewBox="0 0 14 14" aria-hidden="true"><path fill="#1faa9d" d="M2 5c0-2 1.5-3 5-3s5 1 5 3l-2 1-1-2H5L4 6zM3 7h8l1 5H2z"/></svg>
        (855) LUMI-VAL
      </li>
      <li>
        <svg viewBox="0 0 14 14" aria-hidden="true"><path fill="#1faa9d" d="M4 1h6v4H4zM1 6h12v5h-2v2H3v-2H1zM4 9v3h6V9z"/></svg>
        (330) 555-0142
      </li>
      <li>
        <svg viewBox="0 0 14 14" aria-hidden="true"><circle cx="7" cy="7" r="5.5" fill="none" stroke="#1faa9d" stroke-width="1.4"/><path d="M1.5 7h11M7 1.5c-3 3-3 8 0 11M7 1.5c3 3 3 8 0 11" fill="none" stroke="#1faa9d" stroke-width="1.2"/></svg>
        <span>www.<span class="accent">Lumivale</span>.net</span>
      </li>
      <li>
        <svg viewBox="0 0 14 14" aria-hidden="true"><rect x="1" y="3" width="12" height="8" fill="#1faa9d"/><path d="M1 3l6 5 6-5" fill="none" stroke="#1d1d1f" stroke-width="1.2"/></svg>
        Lumivale512@brindlemail.net
      </li>
    </ul>
  </section>

</main>
</body>
</html>
```